SHOPIFY Store Website- complete design and functionality

I am looking for someone to create a modern and clean looking e-commerce store for our new holiday lighting and decor distribution company through Shopify. We will have a variety of products - greenery (wreaths, garland by size), bows, lighting (different types of lighting - c9 bulbs in various colors, 5mm mini lights, c7) and a variety of accessories needed to install your own lighting and decor.

Need to be complete- ready to use.
thx
Updates

We want a fully functional design including set up on Shopify. Assuming we can give you our Shopify password to get it all set up? Have never done this. Please let us know how it works and what an estimated cost would be or what other details you need to provide pricing estimate. thanks

Target Market(s)

Lighting

Font styles to use
Serif
Sans Serif

Requirements
Must have
• A clean and easy to use interface. We have a shopping cart listed on Shopify already. We would like the website to match our company logo as well.

```html
<!DOCTYPE html>
<html lang="en">
<head>
<meta charset="utf-8">
<title>Glowfield Lights – Holiday Lighting &amp; Decor</title>
<link href="https://fonts.googleapis.com/css2?family=Nunito:wght@400;600;700;800;900&family=Nunito+Sans:wght@400;600;700&family=Playfair+Display:ital@1&display=swap" rel="stylesheet">
<style>
:root{
  --orange:#f26b1d;
  --teal:#3f9db1;
  --blue:#1f6fb5;
  --ink:#111;
  --text:#555;
  --muted:#999;
  --line:#ececec;
  --footer:#1b1b1b;
  --card:#f3f3f3;
}
*{margin:0;padding:0;box-sizing:border-box}
html,body{width:1200px;height:3988px;overflow:hidden;background:#fff}
body{position:relative;font-family:"Nunito Sans",Arial,sans-serif;color:var(--text)}
.abs{position:absolute}
h1,h2,h3{font-family:"Nunito",Arial,sans-serif;font-weight:900;color:var(--ink)}

/* header */
.brand{left:96px;top:46px;font-family:"Nunito",sans-serif;font-weight:900;font-size:40px;color:var(--blue);letter-spacing:1px;line-height:1}
.brand small{display:block;font-size:15px;letter-spacing:8px;margin-top:4px;padding-left:68px}
.search{left:692px;top:43px;width:234px;height:40px;border-radius:20px;background:#f4f4f4;font-size:11px;color:#aaa;padding:13px 18px}
.search svg{position:absolute;right:16px;top:12px}
.hicon{top:52px}
.badge{left:1095px;top:31px;width:16px;height:16px;border-radius:50%;background:#c00;color:#fff;font-size:9px;text-align:center;line-height:16px;font-weight:700}
.hrule{left:96px;top:125px;width:1018px;height:1px;background:var(--line)}
.nav{left:98px;top:150px;display:flex;gap:33px;font-size:11px;font-weight:700;color:var(--ink)}
.social{display:flex;gap:14px}
.social i{display:block;width:10px;height:10px;border-radius:50%;background:#c6c6c6}
.lang{left:1042px;top:140px;font-size:11px;font-weight:700;color:var(--ink);display:flex;align-items:center;gap:8px}
.lang span{width:26px;height:26px;border-radius:50%;background:#2c3f8c;display:block}

/* hero */
.hero{left:0;top:190px;width:1200px;height:582px;background:radial-gradient(circle at 82% 40%,#3d5a2a 0,#6b4a22 22%,transparent 45%),linear-gradient(100deg,#c9521a 0%,#e0874a 45%,#b86a3a 70%,#6e4020 100%)}
.hero-title{left:103px;top:345px;color:#fff;font-size:52px;line-height:62px;letter-spacing:.5px}
.hero-text{left:103px;top:482px;width:520px;color:#fff;font-size:12.5px;line-height:21px}
.btn{height:40px;border-radius:20px;font-size:11px;font-weight:800;display:flex;align-items:center;justify-content:center;gap:6px}
.btn-light{left:107px;top:568px;width:160px;background:#fff;color:var(--ink)}
.btn-ghost{left:281px;top:568px;width:160px;border:2px solid #fff;color:#fff}

/* welcome */
.welcome{left:0;top:880px;width:1200px;text-align:center}
.welcome h2{font-size:42px;letter-spacing:1px}
.welcome p{width:690px;margin:26px auto 0;font-size:11.5px;line-height:19px}

/* categories */
.tile{overflow:hidden;color:#fff}
.tile .ex{font-family:"Playfair Display",serif;font-style:italic;font-size:20px}
.tile .nm{font-family:"Nunito",sans-serif;font-weight:900;font-size:17px;letter-spacing:.5px}
.c9{left:104px;top:1110px;width:490px;height:490px;background:linear-gradient(180deg,#2a3a3a 0%,#4a5f7a 35%,#3e9fb3 60%,#3e9fb3 100%);text-align:center}
.c9 .ex{position:absolute;top:272px;width:100%}
.c9 .nm{position:absolute;top:305px;width:100%;font-size:42px}
.c9 p{position:absolute;top:375px;left:130px;width:230px;font-size:11px;line-height:18px}
.garland{left:606px;top:1110px;width:232px;height:240px;background:linear-gradient(160deg,#4a5a20,#9aad70 60%,#c9d7a4)}
.garland .ex{position:absolute;left:26px;top:165px}
.garland .nm{position:absolute;left:26px;top:193px}
.jar{left:606px;top:1360px;width:232px;height:240px;background:radial-gradient(circle at 50% 60%,#e9a847 0,#7a6a55 30%,#2f4560 65%,#c9d4e0 100%)}
.greenery{left:850px;top:1110px;width:232px;height:490px;background:linear-gradient(180deg,#0a0a14 0%,#1a2a40 35%,#2c7a3a 65%,#7a2a8a 100%);text-align:center}
.greenery .ex{position:absolute;top:52px;width:100%}
.greenery .nm{position:absolute;top:80px;width:100%}

/* products */
.products-title{left:0;top:1680px;width:1200px;text-align:center;font-size:42px}
.tabs{left:319px;top:1762px;display:flex;font-size:12px;font-weight:700;color:#777}
.tabs span{padding:0 0 12px;margin-right:50px}
.tabs .on{color:var(--ink);border-bottom:2px solid var(--orange);padding-left:12px;padding-right:12px}
.pimg{width:231px;height:230px}
.pinfo{width:231px;font-size:11px}
.pinfo b{display:block;font-family:"Nunito",sans-serif;font-size:13px;color:var(--ink);font-weight:800}
.pinfo .d{margin-top:4px;color:#777}
.pinfo .pr{margin-top:8px;font-family:"Nunito",sans-serif;font-weight:800;font-size:13px;color:var(--ink)}
.pinfo svg.bag{position:absolute;right:6px;top:0}
.stars{position:absolute;right:4px;top:42px;color:#ccc;font-size:10px;letter-spacing:1px}

/* subscribe */
.sub{left:121px;top:2587px;width:968px;height:128px;background:var(--orange);color:#fff}
.sub h3{position:absolute;left:48px;top:30px;color:#fff;font-size:30px}
.sub p{position:absolute;left:48px;top:72px;font-size:11px}
.sub .field{position:absolute;left:424px;top:42px;width:472px;height:44px;border:2px solid #fff;border-radius:22px;font-size:11px;padding:13px 22px}
.sub .field svg{position:absolute;right:26px;top:9px}

/* testimonials */
.testi{left:0;top:2770px;width:1200px;height:582px;background:linear-gradient(100deg,#5aa8b6 0%,#479aab 55%,#3a8ea1 100%)}
.portrait{left:200px;top:2800px;width:380px;height:552px;background:linear-gradient(180deg,#c79a66 0%,#d9b48c 40%,#b9c4c3 75%,#a9b5b5 100%);border-radius:190px 190px 0 0}
.testi-copy{left:690px;top:2920px;width:320px;text-align:center;color:#fff}
.testi-copy h2{color:#fff;font-size:42px}
.quote{font-family:"Playfair Display",serif;font-size:110px;line-height:80px;height:70px;margin-top:18px}
.testi-copy p{font-size:11.5px;line-height:19px;margin-top:16px}
.testi-copy .who{margin-top:30px;font-size:11px}
.testi-copy .who b{font-family:"Nunito",sans-serif;font-size:13px;margin-right:8px}

/* partners */
.partners{left:140px;top:3415px;width:920px;display:flex;justify-content:space-between;align-items:center}
.partners i{display:block;width:80px;height:58px;background:#d8d8d8;border-radius:6px}
.partners i.rd{border-radius:50%;width:58px}

/* footer */
.footer{left:0;top:3535px;width:1200px;height:453px;background:var(--footer);color:#8a8a8a;font-size:11px}
.flogo{left:96px;top:3652px;color:#fff;font-family:"Nunito",sans-serif;font-weight:900;font-size:40px;line-height:1}
.flogo small{display:block;font-size:15px;letter-spacing:8px;margin-top:4px;padding-left:68px}
.fabout{left:96px;top:3723px;width:300px;line-height:19px;font-size:11px;color:#8a8a8a}
.fmail{left:96px;top:3770px;width:262px;height:42px;border-radius:21px;background:#fff;color:#444;padding:13px 20px;font-size:11px}
.fmail svg{position:absolute;right:18px;top:9px}
.fsocial{left:96px;top:3855px}
.fsocial i{background:#d8d8d8}
.copy{left:96px;top:3893px;font-size:10px;color:#8a8a8a}
.fh{font-family:"Nunito",sans-serif;font-weight:800;font-size:13px;color:#fff}
.crow{left:508px;display:flex;gap:14px;line-height:18px;font-size:11px;color:#8a8a8a}
.crow b{color:#fff;display:block}
.policies{left:870px;top:3680px;line-height:31px;font-size:11px;color:#8a8a8a}
.pay{left:870px;top:3843px;display:flex;gap:26px;font-family:"Nunito",sans-serif;font-weight:800;font-size:15px;color:#8a8a8a}
</style>
</head>
<body>

<!-- Header -->
<div class="abs brand">GLOWFIELD<small>LIGHTS</small></div>
<div class="abs search">Enter your keyword
  <svg width="14" height="14" viewBox="0 0 14 14"><circle cx="8" cy="6" r="4.5" fill="none" stroke="#222" stroke-width="1.8"/><path d="M5 9 1.5 12.5" stroke="#222" stroke-width="2"/></svg>
</div>
<svg class="abs hicon" style="left:966px" width="22" height="24" viewBox="0 0 22 24"><circle cx="11" cy="7" r="5.5" fill="none" stroke="#222" stroke-width="1.8"/><path d="M2 23c0-5 4-8 9-8s9 3 9 8z" fill="none" stroke="#222" stroke-width="1.8"/></svg>
<svg class="abs hicon" style="left:1030px;top:55px" width="24" height="20" viewBox="0 0 24 20"><path d="M12 19 3 10A5 5 0 0 1 12 4a5 5 0 0 1 9 6z" fill="none" stroke="#222" stroke-width="1.8"/></svg>
<svg class="abs hicon" style="left:1094px;top:50px" width="20" height="24" viewBox="0 0 20 24"><rect x="2" y="7" width="16" height="15" fill="none" stroke="#222" stroke-width="1.8"/><path d="M6 9V5a4 4 0 0 1 8 0v4" fill="none" stroke="#222" stroke-width="1.8"/></svg>
<div class="abs badge">0</div>
<div class="abs hrule"></div>
<nav class="abs nav"><span>HOME</span><span>ABOUT US</span><span>PRODUCTS ⌄</span><span>BLOG</span></nav>
<div class="abs social" style="left:890px;top:152px" aria-label="Social links"><i></i><i></i><i></i><i></i></div>
<div class="abs lang"><span role="img" aria-label="Currency flag"></span>GBP ⌄</div>

<!-- Hero -->
<section class="abs hero" role="img" aria-label="Christmas tree branches with warm glowing bokeh lights and ornaments"></section>
<h1 class="abs hero-title">HOLIDAY<br>LIGHTING &amp; DECOR</h1>
<p class="abs hero-text">We will have a variety of products - greenery (wreaths, garland by size), bows, lighting (different types of lighting - c9 bulbs in various colors, 5mm mini lights, c7) and a variety of accessories needed to install your own lighting and decor.</p>
<div class="abs btn btn-light">LEARN MORE</div>
<div class="abs btn btn-ghost"><svg width="14" height="14" viewBox="0 0 14 14"><circle cx="8" cy="6" r="4.5" fill="none" stroke="#fff" stroke-width="1.8"/><path d="M5 9 1.5 12.5" stroke="#fff" stroke-width="2"/></svg>SUPPLIES</div>

<!-- Welcome -->
<section class="abs welcome">
  <h2>WELCOME</h2>
  <p>We will have a variety of products - greenery (wreaths, garland by size), bows, lighting (different types of lighting - c9 bulbs in various colors, 5mm mini lights, c7) and a variety of accessories needed to install your own lighting and decor.</p>
</section>

<!-- Categories -->
<div class="abs tile c9" role="img" aria-label="Colourful C9 bulbs on a string over a teal background">
  <div class="ex">Explore Now</div><div class="nm">C9 BULBS</div>
  <p>Different types of lighting - c9 bulbs in various colors, 5mm mini lights, c7</p>
</div>
<div class="abs tile garland" role="img" aria-label="Pine cone on evergreen garland"><div class="ex">Explore Now</div><div class="nm">GARLAND</div></div>
<div class="abs tile jar" role="img" aria-label="Glass lantern with a glowing star in the snow"></div>
<div class="abs tile greenery" role="img" aria-label="Trees wrapped in green and purple lights at night"><div class="ex">Explore Now</div><div class="nm">GREENERY</div></div>

<!-- Products -->
<h2 class="abs products-title">PRODUCTS</h2>
<div class="abs tabs"><span class="on">GREENERY</span><span>WREATHS</span><span>GARLAND</span><span>BOWS</span><span>ACCESSORIES</span></div>

<div class="abs pimg" style="left:121px;top:1832px;background:radial-gradient(circle,#f3e4d8 35%,#b89a8a 45%,#f1ddd0 58%)" role="img" aria-label="Dried flower wreath"></div>
<div class="abs pimg" style="left:367px;top:1832px;background:radial-gradient(ellipse at 50% 50%,#e6a13a 0,#4c7ad0 25%,#f4f4f4 48%)" role="img" aria-label="Row of coloured C9 bulbs"></div>
<div class="abs pimg" style="left:613px;top:1832px;background:radial-gradient(circle at 50% 60%,#f0f0f0 30%,#d9738d 40%,#efefef 52%)" role="img" aria-label="Flower garland"></div>
<div class="abs pimg" style="left:860px;top:1832px;background:radial-gradient(ellipse,#2d4a40 0,#b44 25%,#f4f4f4 48%)" role="img" aria-label="String of C9 bulbs on green wire"></div>

<div class="abs pimg" style="left:121px;top:2185px;background:radial-gradient(ellipse,#1e4a40 0,#1e4a40 25%,#e8c23a 32%,#f4f4f4 48%)" role="img" aria-label="5mm mini lights"></div>
<div class="abs pimg" style="left:367px;top:2185px;background:radial-gradient(ellipse,#b36a9a 0,#d9a8be 20%,#f3f3f3 40%)" role="img" aria-label="Rose garland"></div>
<div class="abs pimg" style="left:613px;top:2185px;background:radial-gradient(ellipse,#5a1a6e 0,#7a2c90 14%,#f4f4f4 28%)" role="img" aria-label="Purple C9 bulb"></div>
<div class="abs pimg" style="left:860px;top:2185px;background:radial-gradient(circle,#f4f4f4 20%,#2c4a22 30%,#3f5e2a 44%,#f4f4f4 52%)" role="img" aria-label="Evergreen wreath with gold bow"></div>

<div class="abs pinfo" style="left:121px;top:2088px"><b>Wreaths</b><div class="d">Lorem ipsum dolor sit</div><div class="pr">$ 30.00</div><svg class="bag" width="18" height="22" viewBox="0 0 18 22"><rect x="2" y="7" width="14" height="13" fill="none" stroke="#222" stroke-width="1.6"/><path d="M5.5 9V5a3.5 3.5 0 0 1 7 0v4" fill="none" stroke="#222" stroke-width="1.6"/></svg><span class="stars">☆☆☆☆☆</span></div>
<div class="abs pinfo" style="left:370px;top:2088px"><b>C9 bulbs</b><div class="d">Lorem ipsum dolor sit</div><div class="pr">$ 17.99</div><svg class="bag" width="18" height="22" viewBox="0 0 18 22"><rect x="2" y="7" width="14" height="13" fill="none" stroke="#222" stroke-width="1.6"/><path d="M5.5 9V5a3.5 3.5 0 0 1 7 0v4" fill="none" stroke="#222" stroke-width="1.6"/></svg><span class="stars">☆☆☆☆☆</span></div>
<div class="abs pinfo" style="left:615px;top:2088px"><b>Garland</b><div class="d">Lorem ipsum dolor sit</div><div class="pr">$ 30.00</div><svg class="bag" width="18" height="22" viewBox="0 0 18 22"><rect x="2" y="7" width="14" height="13" fill="none" stroke="#222" stroke-width="1.6"/><path d="M5.5 9V5a3.5 3.5 0 0 1 7 0v4" fill="none" stroke="#222" stroke-width="1.6"/></svg><span class="stars">☆☆☆☆☆</span></div>
<div class="abs pinfo" style="left:863px;top:2088px"><b>C9 bulbs</b><div class="d">Lorem ipsum dolor sit</div><div class="pr">$ 30.00</div><svg class="bag" width="18" height="22" viewBox="0 0 18 22"><rect x="2" y="7" width="14" height="13" fill="none" stroke="#222" stroke-width="1.6"/><path d="M5.5 9V5a3.5 3.5 0 0 1 7 0v4" fill="none" stroke="#222" stroke-width="1.6"/></svg><span class="stars">☆☆☆☆☆</span></div>

<div class="abs pinfo" style="left:121px;top:2441px"><b>5mm mini lights</b><div class="d">Lorem ipsum dolor sit</div><div class="pr">$ 30.00</div><svg class="bag" width="18" height="22" viewBox="0 0 18 22"><rect x="2" y="7" width="14" height="13" fill="none" stroke="#222" stroke-width="1.6"/><path d="M5.5 9V5a3.5 3.5 0 0 1 7 0v4" fill="none" stroke="#222" stroke-width="1.6"/></svg><span class="stars">☆☆☆☆☆</span></div>
<div class="abs pinfo" style="left:370px;top:2441px"><b>Garland</b><div class="d">Lorem ipsum dolor sit</div><div class="pr">$ 17.99</div><svg class="bag" width="18" height="22" viewBox="0 0 18 22"><rect x="2" y="7" width="14" height="13" fill="none" stroke="#222" stroke-width="1.6"/><path d="M5.5 9V5a3.5 3.5 0 0 1 7 0v4" fill="none" stroke="#222" stroke-width="1.6"/></svg><span class="stars">☆☆☆☆☆</span></div>
<div class="abs pinfo" style="left:615px;top:2441px"><b>C9 bulbs</b><div class="d">Lorem ipsum dolor sit</div><div class="pr">$ 30.00</div><svg class="bag" width="18" height="22" viewBox="0 0 18 22"><rect x="2" y="7" width="14" height="13" fill="none" stroke="#222" stroke-width="1.6"/><path d="M5.5 9V5a3.5 3.5 0 0 1 7 0v4" fill="none" stroke="#222" stroke-width="1.6"/></svg><span class="stars">☆☆☆☆☆</span></div>
<div class="abs pinfo" style="left:863px;top:2441px"><b>Wreaths</b><div class="d">Lorem ipsum dolor sit</div><div class="pr">$ 30.00</div><svg class="bag" width="18" height="22" viewBox="0 0 18 22"><rect x="2" y="7" width="14" height="13" fill="none" stroke="#222" stroke-width="1.6"/><path d="M5.5 9V5a3.5 3.5 0 0 1 7 0v4" fill="none" stroke="#222" stroke-width="1.6"/></svg><span class="stars">☆☆☆☆☆</span></div>

<!-- Subscribe -->
<section class="abs sub">
  <h3>SUBSCRIBE TODAY!</h3>
  <p>Be the First to Know. Sign up for newsletter today</p>
  <div class="field">Enter your email address
    <svg width="28" height="22" viewBox="0 0 28 22"><path d="M1 10 27 1 19 21 13 13z" fill="#fff"/><path d="M13 13 27 1" stroke="var(--orange)" stroke-width="1.5"/></svg>
  </div>
</section>

<!-- Testimonials -->
<section class="abs testi"></section>
<div class="abs portrait" role="img" aria-label="Portrait of a smiling customer wearing a flower crown"></div>
<div class="abs testi-copy">
  <h2>TESTIMONIALS</h2>
  <div class="quote">“</div>
  <p>Lorem ipsum dolor sit amet, consectetur adipiscing elit. Donec eu odio urna. Cras neque sem, imperdiet accumsan ante vel, ornare cursus enim. Curabitur vitae tellus tempus, mollis odio eget, finibus urna.</p>
  <div class="who"><b>Mara Ellison</b> - Athelete</div>
</div>

<!-- Partners -->
<div class="abs partners" aria-label="Partner badges"><i class="rd"></i><i class="rd"></i><i></i><i></i><i></i><i class="rd"></i></div>

<!-- Footer -->
<footer class="abs footer"></footer>
<div class="abs flogo">GLOWFIELD<small>LIGHTS</small></div>
<p class="abs fabout">Lorem ipsum dolor sit amet, consectetur adipiscing elit. Donec eu odio urna. Cras neque sem.</p>
<div class="abs fmail">Enter your email address
  <svg width="28" height="22" viewBox="0 0 28 22"><path d="M1 10 27 1 19 21 13 13z" fill="var(--orange)"/><path d="M13 13 27 1" stroke="#fff" stroke-width="1.5"/></svg>
</div>
<div class="abs social fsocial" aria-label="Social links"><i></i><i></i><i></i><i></i></div>
<div class="abs copy">Copyright © 2021 Glowfield Lights</div>

<div class="abs fh" style="left:513px;top:3628px">CONTACT US</div>
<div class="abs crow" style="top:3680px">
  <svg width="20" height="20" viewBox="0 0 20 20"><path d="M4 2l3 4-2 2a11 11 0 0 0 7 7l2-2 4 3-2 3C8 19 1 12 1 4z" fill="none" stroke="#aaa" stroke-width="1.4"/></svg>
  <div>Call Customer Services, We Support 24/7 :<b>555-014-2290</b></div>
</div>
<div class="abs crow" style="top:3757px">
  <svg width="20" height="22" viewBox="0 0 20 22"><path d="M10 21s7-7 7-12A7 7 0 0 0 3 9c0 5 7 12 7 12z" fill="none" stroke="#aaa" stroke-width="1.4"/><circle cx="10" cy="9" r="2.5" fill="none" stroke="#aaa" stroke-width="1.4"/></svg>
  <div><b>Address :</b>PO Box 4410 Lantern Row West</div>
</div>
<div class="abs crow" style="top:3830px">
  <svg width="22" height="16" viewBox="0 0 22 16"><rect x="1" y="1" width="20" height="14" fill="none" stroke="#aaa" stroke-width="1.4"/><path d="M1 1l10 8 10-8" fill="none" stroke="#aaa" stroke-width="1.4"/></svg>
  <div><b>Email :</b>hello@glowfield.shop</div>
</div>

<div class="abs fh" style="left:870px;top:3628px">OUR POLICIES</div>
<div class="abs policies">Privacy Policy<br>Refund Policy<br>Terms of Service<br>Shipping Policy</div>
<div class="abs pay"><span>CardOne</span><span>PayLine</span><span>Expressa</span></div>

</body>
</html>
```